On going F & B business needs a new stationery design for a festive occasion

basically it is an envelope where money is inserted and given out to friends and relatives on the festive occasion of "EID MUBARAK"
Attached is my 2017 design and actual. Need something more up to date and refreshing. Have also attached my company logo files. Would prefer to have the overall design in Green and Yellow,

Industry/Entity Type

Business

Colors
acd036
fbee3d

```html
<!DOCTYPE html>
<html lang="en">
<head>
<meta charset="utf-8">
<title>Noor Harvest Kitchen – Eid Mubarak Money Envelope</title>
<link rel="stylesheet" href="https://fonts.googleapis.com/css2?family=Open+Sans:wght@400;600;800&family=Marck+Script&display=swap">
<style>
  :root {
    --paper: #ffffff;
    --envelope-green: #1f7352;
    --envelope-green-light: #26805c;
    --green-ink: #1d6a45;
    --festive-yellow: #f6cb2e;
    --deep-gold: #e0ad1c;
    --flap-yellow: #f5cd2c;
    --rule-white: #ffffff;
  }
  * { margin: 0; padding: 0; box-sizing: border-box; }
  html, body {
    width: 1200px; height: 1000px; overflow: hidden;
    background: var(--paper);
  }
  .canvas { position: relative; width: 1200px; height: 1000px; }
  .dieline { position: absolute; inset: 0; }

  .flap-brand {
    position: absolute; left: 690px; top: 132px; width: 190px;
    transform: rotate(180deg);
    display: flex; align-items: center; gap: 10px;
    font-family: "Open Sans", sans-serif; font-weight: 800;
    color: var(--green-ink); line-height: 1.1;
  }
  .flap-brand .brand-dot {
    width: 28px; height: 28px; border-radius: 50%;
    background: var(--green-ink); flex: none;
  }
  .flap-brand .brand-name { font-size: 17px; letter-spacing: 1.5px; }

  .contact {
    position: absolute; left: 221px; top: 721px;
    font-family: "Open Sans", sans-serif; font-size: 13.5px;
    font-style: normal;
    color: var(--festive-yellow); line-height: 18.5px;
  }
  .contact-row { display: flex; align-items: flex-start; gap: 5px; }
  .contact-row svg { flex: none; margin-top: 3px; }
  .contact .address { margin-bottom: 5px; }
  .contact .phone { margin-bottom: 2px; }
  .contact .website { margin-top: 14px; font-weight: 600; }

  .greeting {
    position: absolute; left: 612px; top: 796px;
    font-family: "Marck Script", cursive; font-weight: 400;
    font-size: 55px; letter-spacing: 1px;
    color: var(--festive-yellow);
  }
</style>
</head>
<body>
<main class="canvas">
  <svg class="dieline" width="1200" height="1000" viewBox="0 0 1200 1000">
    <defs>
      <linearGradient id="lanternGlow" x1="0" y1="0" x2="0" y2="1">
        <stop offset="0" stop-color="var(--festive-yellow)"/>
        <stop offset="0.55" stop-color="#f3c52a"/>
        <stop offset="1" stop-color="var(--deep-gold)"/>
      </linearGradient>
      <radialGradient id="mandalaGlow" cx="0.5" cy="0.5" r="0.5">
        <stop offset="0" stop-color="var(--festive-yellow)" stop-opacity="0.95"/>
        <stop offset="0.5" stop-color="var(--festive-yellow)" stop-opacity="0.75"/>
        <stop offset="0.8" stop-color="#d8b53a" stop-opacity="0.45"/>
        <stop offset="1" stop-color="#d8b53a" stop-opacity="0"/>
      </radialGradient>
      <radialGradient id="cornerOrnament" cx="0.5" cy="0.5" r="0.5">
        <stop offset="0" stop-color="#4f9a78" stop-opacity="0.45"/>
        <stop offset="1" stop-color="#4f9a78" stop-opacity="0"/>
      </radialGradient>
      <linearGradient id="bodyTone" x1="0" y1="0" x2="1" y2="1">
        <stop offset="0" stop-color="var(--envelope-green)"/>
        <stop offset="0.5" stop-color="var(--envelope-green-light)"/>
        <stop offset="1" stop-color="var(--envelope-green)"/>
      </linearGradient>
      <clipPath id="bodyClip">
        <path d="M205,215 L975,215 L995,236 L995,872 L930,938 L775,938 L730,895 L205,895 Z"/>
      </clipPath>
    </defs>

    <!-- top flap -->
    <path class="flap" fill="var(--flap-yellow)"
      d="M588,215 L588,196 C588,170 610,150 640,146 C662,100 705,62 780,62 C855,62 898,100 920,146 C950,150 972,170 972,196 L972,215 Z"/>

    <!-- envelope body with bottom tuck flap -->
    <path class="envelope-body" fill="url(#bodyTone)" role="img" aria-label="Green background with subtle Islamic geometric pattern"
      d="M205,215 L975,215 L995,236 L995,872 L930,938 L775,938 L730,895 L205,895 Z"/>

    <!-- faint corner ornaments -->
    <g class="corner-ornaments" clip-path="url(#bodyClip)">
      <circle role="img" aria-label="Faint floral ornament, top right corner" cx="975" cy="300" r="115" fill="url(#cornerOrnament)"/>
      <circle role="img" aria-label="Faint floral ornament, bottom left corner" cx="255" cy="735" r="120" fill="url(#cornerOrnament)"/>
      <circle role="img" aria-label="Faint floral ornament, bottom right corner" cx="955" cy="850" r="120" fill="url(#cornerOrnament)"/>
    </g>

    <!-- name line -->
    <line class="name-rule" x1="291" y1="299" x2="503" y2="299" stroke="var(--rule-white)" stroke-width="2"/>

    <!-- lantern strings -->
    <g class="lantern-strings" stroke="var(--festive-yellow)" stroke-width="1.3">
      <line x1="267" y1="215" x2="267" y2="435"/>
      <line x1="351" y1="215" x2="351" y2="555"/>
      <line x1="467" y1="215" x2="467" y2="360"/>
      <line x1="549" y1="215" x2="549" y2="450"/>
      <line x1="638" y1="540" x2="638" y2="660"/>
      <line x1="685" y1="575" x2="685" y2="728"/>
      <line x1="878" y1="575" x2="878" y2="695"/>
      <line x1="922" y1="540" x2="922" y2="660"/>
    </g>

    <!-- lantern illustrations -->
    <g class="lanterns" fill="url(#lanternGlow)">
      <rect role="img" aria-label="Hanging Ramadan lantern illustration" x="236" y="435" width="64" height="185" rx="14"/>
      <rect role="img" aria-label="Small hanging lantern illustration" x="335" y="555" width="32" height="85" rx="8"/>
      <rect role="img" aria-label="Hanging Ramadan lantern illustration" x="434" y="360" width="66" height="185" rx="14"/>
      <rect role="img" aria-label="Small hanging lantern illustration" x="533" y="450" width="32" height="85" rx="8"/>
      <rect role="img" aria-label="Hanging lantern illustration" x="620" y="660" width="36" height="102" rx="9"/>
      <rect role="img" aria-label="Small hanging lantern illustration" x="675" y="728" width="19" height="47" rx="5"/>
      <rect role="img" aria-label="Small hanging lantern illustration" x="870" y="695" width="17" height="40" rx="5"/>
      <rect role="img" aria-label="Hanging lantern illustration" x="905" y="660" width="35" height="102" rx="9"/>
    </g>

    <!-- mandala with Arabic Eid calligraphy -->
    <circle role="img" aria-label="Golden floral mandala ornament framing Arabic Eid Mubarak calligraphy"
      cx="780" cy="475" r="145" fill="url(#mandalaGlow)"/>
  </svg>

  <div class="flap-brand">
    <span class="brand-dot"></span>
    <span class="brand-name">NOOR HARVEST<br>KITCHEN</span>
  </div>

  <address class="contact">
    <div class="contact-row address">
      <svg width="10" height="12" viewBox="0 0 10 12"><path d="M5,0.8 C2.6,0.8 1,2.5 1,4.6 C1,7.3 5,11.2 5,11.2 C5,11.2 9,7.3 9,4.6 C9,2.5 7.4,0.8 5,0.8 Z" fill="none" stroke="var(--festive-yellow)" stroke-width="1.4"/><circle cx="5" cy="4.6" r="1.4" fill="var(--festive-yellow)"/></svg>
      <span>Beside Harbourfront Walk<br>18 Cedar Grove Industrial<br>Park Road 2 #02-07<br>Singapore 648310</span>
    </div>
    <div class="contact-row phone">
      <svg width="10" height="10" viewBox="0 0 10 10"><path d="M2,0.5 L3.8,2.8 L2.8,4 C3.5,5.4 4.6,6.5 6,7.2 L7.2,6.2 L9.5,8 L8.4,9.5 C4.4,9.2 0.8,5.6 0.5,1.6 Z" fill="var(--festive-yellow)"/></svg>
      <span>61284573</span>
    </div>
    <div class="contact-row email">
      <svg width="10" height="9" viewBox="0 0 10 9"><rect x="0.5" y="1" width="9" height="7" fill="var(--festive-yellow)"/><path d="M0.5,1.5 L5,5 L9.5,1.5" fill="none" stroke="var(--envelope-green)" stroke-width="1"/></svg>
      <span>hello@noorharvest.com.sg</span>
    </div>
    <div class="website">www.noorharvest.com.sg</div>
  </address>

  <h1 class="greeting">Eid Mubarak</h1>
</main>
</body>
</html>
```